BPR Business Card

We need a business card that reflect our business, we have put anther business card as an example of what we like but please feel free to do your own thing.

Here are the items to be placed on card

Glen Harwick
Bright Parcel Route
Mobile: 917-555-4862
Office: 516-555-7104
Fax: 866-555-3927
Email: info@brightparcelroute.example
Website: brightparcelroute.example

I have added raw files to upload

Glen Harwick
Bright Parcel Route
Mobile: 917-555-4862
Office: 516-555-7104
Fax: 866-555-3927 

Target Market(s)

Natural product manufactures, and retailers and distributors

Industry/Entity Type

Business

Requirements
Must have
• 1. Logo
2. The colors of the company

```html
<!DOCTYPE html>
<html lang="en">
<head>
<meta charset="utf-8">
<title>Bright Parcel Route – Business Card</title>
<link rel="stylesheet" href="https://fonts.googleapis.com/css2?family=Open+Sans:wght@400;600;700;800&display=swap">
<style>
  :root {
    --green-light: #93c975;
    --green: #5cb346;
    --green-deep: #3f9c35;
    --ink: #2b2b2b;
    --grey-line: #c9c9c9;
    --paper: #ffffff;
    --paper-shade: #eeeeee;
    --stage: #e9e7e2;
  }
  html, body {
    margin: 0;
    width: 1200px;
    height: 750px;
    overflow: hidden;
    background: var(--stage);
    font-family: "Open Sans", Arial, sans-serif;
  }
  .canvas {
    position: relative;
    width: 1200px;
    height: 750px;
    display: flex;
    align-items: center;
    justify-content: center;
    gap: 50px;
  }
  .card {
    width: 540px;
    height: 309px;
    box-shadow: 0 8px 24px rgba(0,0,0,0.18);
    display: block;
  }
  .card svg { display: block; width: 540px; height: 309px; }
  .brand-name { font-weight: 800; fill: var(--green); }
  .company-strong { font-weight: 700; fill: var(--green); }
  .company-light { font-weight: 400; fill: var(--ink); }
  .tagline { font-weight: 400; fill: var(--ink); font-size: 10.5px; }
  .person-first { font-weight: 700; fill: var(--paper); }
  .person-last { font-weight: 400; fill: var(--paper); }
  .contact { font-weight: 400; fill: var(--ink); font-size: 10.5px; }
</style>
</head>
<body>
<main class="canvas">

  <!-- Front of card -->
  <div class="card card-front">
    <svg viewBox="0 0 540 309" xmlns="http://www.w3.org/2000/svg" font-family="Open Sans, Arial, sans-serif">
      <defs>
        <linearGradient id="front-green" x1="0" y1="0" x2="0" y2="1">
          <stop offset="0" stop-color="var(--green-light)"/>
          <stop offset="1" stop-color="var(--green-deep)"/>
        </linearGradient>
        <pattern id="hatch" width="5" height="5" patternUnits="userSpaceOnUse" patternTransform="rotate(45)">
          <line x1="0" y1="0" x2="0" y2="5" stroke="var(--grey-line)" stroke-width="1.4"/>
        </pattern>
      </defs>
      <rect class="card-base" width="540" height="309" fill="url(#front-green)"/>
      <polygon class="front-band" points="0,88 540,158 540,258 0,188" fill="var(--paper)"/>
      <polygon class="band-edge" points="0,88 540,158 540,164 0,94" fill="url(#hatch)"/>
      <polygon class="band-edge" points="0,182 540,252 540,258 0,188" fill="url(#hatch)"/>
      <g class="front-mark" transform="translate(270 173) rotate(7.4)">
        <rect x="-118" y="-11" width="18" height="18" fill="var(--green)"/>
        <text class="brand-name" x="-92" y="6" font-size="19">Bright Parcel Route</text>
      </g>
    </svg>
  </div>

  <!-- Back of card -->
  <div class="card card-back">
    <svg viewBox="0 0 540 309" xmlns="http://www.w3.org/2000/svg" font-family="Open Sans, Arial, sans-serif">
      <defs>
        <linearGradient id="back-paper" x1="0" y1="0" x2="1" y2="1">
          <stop offset="0" stop-color="var(--paper-shade)"/>
          <stop offset="0.5" stop-color="var(--paper)"/>
          <stop offset="1" stop-color="var(--paper-shade)"/>
        </linearGradient>
        <linearGradient id="band-fade" x1="0" y1="0" x2="1" y2="0">
          <stop offset="0" stop-color="var(--green)"/>
          <stop offset="0.55" stop-color="var(--green-light)"/>
          <stop offset="1" stop-color="var(--paper)" stop-opacity="0"/>
        </linearGradient>
        <linearGradient id="name-band" x1="0" y1="0" x2="1" y2="0">
          <stop offset="0" stop-color="var(--green-light)"/>
          <stop offset="1" stop-color="var(--green)"/>
        </linearGradient>
        <pattern id="hatch-back" width="5" height="5" patternUnits="userSpaceOnUse" patternTransform="rotate(45)">
          <line x1="0" y1="0" x2="0" y2="5" stroke="var(--grey-line)" stroke-width="1.4"/>
        </pattern>
      </defs>
      <rect class="card-base" width="540" height="309" fill="url(#back-paper)"/>

      <polygon class="top-band" points="0,30 540,100 540,124 0,54" fill="url(#band-fade)"/>
      <polygon class="band-edge" points="0,54 540,124 540,129 0,59" fill="url(#hatch-back)"/>

      <polygon class="name-band" points="300,132 540,163 540,210 300,179" fill="url(#name-band)"/>
      <polygon class="band-edge" points="300,179 540,210 540,215 300,184" fill="url(#hatch-back)"/>

      <polygon class="bottom-band" points="0,274 540,294 540,309 0,309" fill="var(--green)"/>
      <polygon class="band-edge" points="0,268 540,288 540,294 0,274" fill="url(#hatch-back)"/>

      <g class="logo-panel" transform="rotate(7.4 200 60)">
        <rect x="138" y="16" width="128" height="88" fill="var(--paper)" stroke="#d4d4d4" stroke-width="5"/>
        <rect x="152" y="52" width="12" height="12" fill="var(--green)"/>
        <text class="brand-name" x="170" y="55" font-size="12">Bright Parcel</text>
        <text class="brand-name" x="170" y="70" font-size="12">Route</text>
      </g>

      <g class="company" transform="rotate(7.4 70 128)">
        <text x="70" y="132" font-size="16">
          <tspan class="company-strong">BRIGHT PARCEL</tspan><tspan class="company-light"> ROUTE</tspan>
        </text>
        <text class="tagline" x="72" y="147">For all your natural product needs</text>
      </g>

      <g class="person" transform="rotate(7.4 525 185)">
        <text x="525" y="192" font-size="18" text-anchor="end">
          <tspan class="person-first">GLEN</tspan><tspan class="person-last"> HARWICK</tspan>
        </text>
      </g>

      <g class="contacts" transform="rotate(7.4 450 230)">
        <text class="contact" x="450" y="218" text-anchor="end">Mobile: 917-555-4862</text>
        <text class="contact" x="450" y="231" text-anchor="end">Office: 516-555-7104</text>
        <text class="contact" x="450" y="244" text-anchor="end">Fax: 866-555-3927</text>
        <text class="contact" x="450" y="259" text-anchor="end">info@brightparcelroute.example</text>
        <text class="contact" x="450" y="272" text-anchor="end">brightparcelroute.example</text>

        <g class="icon-phone" transform="translate(470 234)" fill="var(--ink)">
          <path d="M-9,-3 Q0,-10 9,-3 L7,1 L3,-1 L3,-3 Q0,-5 -3,-3 L-3,-1 L-7,1 Z"/>
          <rect x="-6" y="1" width="12" height="7" rx="1.5"/>
        </g>
        <g class="icon-globe" transform="translate(470 266)" fill="none" stroke="var(--ink)" stroke-width="1.3">
          <circle r="8"/>
          <ellipse rx="3.5" ry="8"/>
          <line x1="-8" y1="0" x2="8" y2="0"/>
          <line x1="-7" y1="-4" x2="7" y2="-4"/>
          <line x1="-7" y1="4" x2="7" y2="4"/>
        </g>
      </g>
    </svg>
  </div>

</main>
</body>
</html>
```